Bellmoor Commercial Finance Information Brochure

This brochure will be sent out to clients via A4 PDF on an email to showcase what our company has to offer. We are a commercial finance brokerage, that specialises in property finance. We would like to see designs following our colour scheme. The final design should demonstrate our professionalism and reliability.
I have attached our logo and also a few bullet points on our information and what we can offer. These can be slightly reworded for conciseness. Or leave the text sections as filler and I can fill these in.
I have also attached an overview of our colour scheme and design styling for your consideration.
Target Market(s)
Property Developers
Industry/Entity Type
Financial Services

```html
<!DOCTYPE html>
<html lang="en">
<head>
<meta charset="utf-8">
<title>Bellmoor Finance – Information Brochure</title>
<link rel="stylesheet" href="https://fonts.googleapis.com/css2?family=Encode+Sans+Condensed:wght@300;400&family=Open+Sans:ital,wght@0,700;1,700;1,800&family=Arimo:wght@400&display=swap">
<style>
  :root{
    --brand-blue:#2f4a8a;
    --brand-blue-deep:#283f78;
    --brand-green:#4f8a43;
    --brand-green-soft:#dfe9dc;
    --ink:#2a2a2a;
    --paper:#ffffff;
    --sky-grey:#d7dbe3;
  }
  *{box-sizing:border-box;margin:0;padding:0}
  html,body{width:1200px;height:564px;overflow:hidden;background:var(--paper)}
  body{position:relative;font-family:"Encode Sans Condensed",sans-serif;color:var(--ink)}

  .page{position:absolute;top:16px;width:371px;height:524px;overflow:hidden}
  .page--cover{left:16px;width:370px;background:var(--brand-blue)}
  .page--inner{background:var(--paper);border:1px solid #c9cfdc}
  .page--services{left:415px}
  .page--strengths{left:811px}

  /* cover */
  .cover-skyline{position:absolute;left:0;right:0;bottom:0;height:230px;
    background:linear-gradient(180deg,rgba(47,74,138,0) 0%,#3a5a9c 45%,#3f67a8 100%)}
  .cover-name{position:absolute;left:0;right:0;top:190px;text-align:center;
    font-family:"Open Sans",sans-serif;font-weight:700;color:var(--paper);
    font-size:34px;line-height:40px;letter-spacing:3px}

  /* inner header */
  .brand-name{position:absolute;left:23px;top:30px;font-family:"Open Sans",sans-serif;
    font-weight:700;color:var(--brand-blue);font-size:17px;line-height:19px;letter-spacing:1px}
  .contact{position:absolute;left:249px;top:13px;padding-left:5px;border-left:1px solid #555;
    font-family:"Arimo",sans-serif;font-size:6.4px;line-height:8.7px;color:#111}
  .contact li{list-style:none;display:flex;align-items:center;gap:3px}
  .contact li.gap{margin-top:3px}
  .contact svg{width:5px;height:5px;flex:none}

  /* sections */
  .section-bar{position:absolute;left:0;right:0;height:22px;
    background:linear-gradient(90deg,var(--brand-green) 0%,#7ea872 45%,var(--brand-green-soft) 85%,#f1f4f0 100%)}
  .section-bar h2{position:absolute;left:23px;top:1px;font-family:"Open Sans",sans-serif;
    font-style:italic;font-weight:800;font-size:15px;line-height:20px;color:var(--paper);
    text-shadow:1px 1px 2px rgba(0,0,0,.35);white-space:nowrap}
  .section-text{position:absolute;left:107px;width:242px;font-weight:300;font-size:10.4px;
    line-height:12.7px;letter-spacing:-0.18px;color:#222}
  .icon{position:absolute;border-radius:3px}

  .city-haze{position:absolute;left:0;right:0;top:330px;height:180px;
    background:linear-gradient(180deg,rgba(215,219,227,0) 0%,var(--sky-grey) 55%,#c3c8d2 100%)}
  .page-foot{position:absolute;left:0;bottom:0;width:371px;height:40px}
</style>
</head>
<body>

  <section class="page page--cover">
    <div class="cover-skyline" role="img" aria-label="Evening city skyline photograph fading into the blue cover"></div>
    <p class="cover-name">BELLMOOR<br>FINANCE</p>
  </section>

  <section class="page page--inner page--services">
    <div class="city-haze" role="img" aria-label="Faded grey city skyline photograph"></div>

    <p class="brand-name">BELLMOOR<br>FINANCE</p>
    <ul class="contact">
      <li>412 Harlow Street</li>
      <li>Northvale, Oregon 97210</li>
      <li class="gap"><svg viewBox="0 0 10 10"><path d="M2 1l2 2-1 1.5 2.5 2.5L7 6l2 2-1.5 1.5C5 9.5.5 5 .5 2.5z" fill="#2f4a8a"/></svg>555-218-4470</li>
      <li><svg viewBox="0 0 10 10"><rect x="2.5" y=".5" width="5" height="9" rx="1" fill="none" stroke="#222"/></svg>555-604-1192</li>
      <li><svg viewBox="0 0 10 10"><rect x=".5" y="2" width="9" height="6" fill="#2f4a8a"/><path d="M.5 2L5 5.5 9.5 2" stroke="#fff" fill="none"/></svg>hello@bellmoorfinance.com</li>
      <li><svg viewBox="0 0 10 10"><circle cx="5" cy="5" r="4.5" fill="#4f8a43"/><path d="M.5 5h9M5 .5v9" stroke="#fff" stroke-width=".8"/></svg>www.bellmoorfinance.com</li>
    </ul>

    <div class="section-bar" style="top:80px"><h2>We take care of your valuable time</h2></div>
    <div class="icon" style="left:32px;top:120px;width:46px;height:61px;background:linear-gradient(180deg,#2f4a8a,#9aa9cf 50%,#2f4a8a)" role="img" aria-label="Hourglass icon"></div>
    <p class="section-text" style="top:112px">As former lenders and developers ourselves, we intimately understand the inefficiencies that plague deals in the market today. We’ve experienced the frustration of tight time limits on deals and the exasperating feeling of brokers wasting precious time collecting information. It’s enough to drive developers and lenders insane!</p>

    <div class="section-bar" style="top:197px"><h2>Connecting with Efficiency and Trust</h2></div>
    <div class="icon" style="left:25px;top:228px;width:72px;height:73px;background:linear-gradient(135deg,#2f4a8a 50%,#4f8a43 50%)" role="img" aria-label="Handshake with bar chart and dollar sign icon"></div>
    <p class="section-text" style="top:222px">That’s why we founded Bellmoor Finance – to be the efficient and reliable link that connects developers and lenders. We’ve streamlined our processes to eliminate unnecessary hurdles, enabling clear and swift communication between all parties involved. No more wasted time. No more unnecessary stress.</p>

    <div class="section-bar" style="top:308px"><h2>Simplified financing journey</h2></div>
    <div class="icon" style="left:23px;top:343px;width:69px;height:54px;background:linear-gradient(90deg,#4f8a43,#2f4a8a)" role="img" aria-label="Three-step icon with light bulb, dollar sign and chart"></div>
    <p class="section-text" style="top:332px">With our expertise and industry insights, we’ve developed a unique approach that simplifies the financing journey. From the initial consultation to the final funding, we’re here to guide you every step of the way. Our goal? To make commercial financing a smooth and enjoyable experience for you.</p>

    <svg class="page-foot" viewBox="0 0 371 40" preserveAspectRatio="none">
      <path d="M0 10 Q190 22 371 0 V40 H0Z" fill="#4f8a43"/>
      <path d="M0 13 Q190 24 371 4 V40 H0Z" fill="#ffffff"/>
      <path d="M0 15 Q190 26 371 6 V40 H0Z" fill="#2f4a8a"/>
    </svg>
  </section>

  <section class="page page--inner page--strengths">
    <div class="city-haze" role="img" aria-label="Faded grey city skyline photograph"></div>

    <p class="brand-name">BELLMOOR<br>FINANCE</p>
    <ul class="contact">
      <li>412 Harlow Street</li>
      <li>Northvale, Oregon 97210</li>
      <li class="gap"><svg viewBox="0 0 10 10"><path d="M2 1l2 2-1 1.5 2.5 2.5L7 6l2 2-1.5 1.5C5 9.5.5 5 .5 2.5z" fill="#2f4a8a"/></svg>555-218-4470</li>
      <li><svg viewBox="0 0 10 10"><rect x="2.5" y=".5" width="5" height="9" rx="1" fill="none" stroke="#222"/></svg>555-604-1192</li>
      <li><svg viewBox="0 0 10 10"><rect x=".5" y="2" width="9" height="6" fill="#2f4a8a"/><path d="M.5 2L5 5.5 9.5 2" stroke="#fff" fill="none"/></svg>hello@bellmoorfinance.com</li>
      <li><svg viewBox="0 0 10 10"><circle cx="5" cy="5" r="4.5" fill="#4f8a43"/><path d="M.5 5h9M5 .5v9" stroke="#fff" stroke-width=".8"/></svg>www.bellmoorfinance.com</li>
    </ul>

    <div class="section-bar" style="top:80px"><h2>Exclusive Book of Investors</h2></div>
    <div class="icon" style="left:42px;top:112px;width:41px;height:51px;background:var(--brand-green)" role="img" aria-label="Green book with dollar sign icon"></div>
    <p class="section-text" style="top:113px">With our background in the asset management industry, we have cultivated a black book of fund managers, institutions, UHNWI and private equity lenders that we can call on for non-traditional lending.</p>

    <div class="section-bar" style="top:175px"><h2>Efficiency</h2></div>
    <div class="icon" style="left:28px;top:202px;width:58px;height:56px;background:linear-gradient(135deg,#2f4a8a 0%,#3f5f95 55%,#4f8a43 100%)" role="img" aria-label="Gear with check mark icon"></div>
    <p class="section-text" style="top:202px">Bellmoor Finance was created to satisfy a need in the market that has been far too overlooked. Efficiency. Efficiency is at the heart of our operations, and we pride ourselves on our ability to secure the best financing options swiftly and effectively for our clients. By employing cutting-edge technology and streamlining our internal processes, we have cultivated a seamless and time-saving approach to finance brokering. Having been a developer, we understand the stresses and headaches associated with building, let alone all the paperwork and emails backwards and forwards between yourself and brokers to attain the necessary financing.</p>

    <div class="section-bar" style="top:346px"><h2>Quality Communication and Information</h2></div>
    <div class="icon" style="left:30px;top:380px;width:58px;height:54px;border-radius:50%;background:linear-gradient(135deg,#4f8a43 55%,#2f4a8a 55%)" role="img" aria-label="Speech bubbles icon"></div>
    <p class="section-text" style="top:380px">We are well-versed in the questions lenders will ask, allowing us to get ahead of the curve and request all the necessary information from you on day one. This approach provides you with a distinct advantage, as it eliminates the need to allocate hours each day to answering questions and fulfilling requests from brokers. By entrusting us with this responsibility, you can focus on your core tasks and leave the financing aspect to us, making the process less stressful for you.</p>

    <svg class="page-foot" viewBox="0 0 371 40" preserveAspectRatio="none">
      <path d="M0 10 Q190 22 371 0 V40 H0Z" fill="#4f8a43"/>
      <path d="M0 13 Q190 24 371 4 V40 H0Z" fill="#ffffff"/>
      <path d="M0 15 Q190 26 371 6 V40 H0Z" fill="#2f4a8a"/>
    </svg>
  </section>

</body>
</html>
```